Luxury Tea Brand Needs Packaging Design

Our team needs a luxe design replicating the shape of the attached picture for a box that will contain drawstring teabags. There is an opportunity for silver or gold reflective design

Please include a design for the

Product dimensions - 10.5x4x9 cm
things to keep in mind

- luxury design
- Mainly black with either silver or gold
- Should say pack of 100
- Should say Leaf of Rivo Tea Filters

some of our products have been attached as a style reference

website is www.leafofrivo.com

Target Market(s)

modern millennials

Requirements
Must have
• luxury feel
Nice to have
• shiny designs

```html
<!DOCTYPE html>
<html lang="en">
<head>
<meta charset="utf-8">
<title>Leaf of Rivo – Tea Filters Box</title>
<link rel="stylesheet" href="https://fonts.googleapis.com/css2?family=Montserrat:wght@600;700&display=swap">
<style>
  :root {
    --backdrop: #e9e6df;
    --box-black: #1b1b1b;
    --box-sheen: #3b3a36;
    --gold: #b8963a;
    --gold-light: #d4b35a;
  }
  * { box-sizing: border-box; margin: 0; padding: 0; }
  html, body {
    width: 1200px; height: 562px; overflow: hidden;
    background: var(--backdrop);
    font-family: "Montserrat", Arial, sans-serif;
  }
  .dieline {
    width: 1200px; height: 562px;
    display: flex; align-items: center; justify-content: center; gap: 60px;
  }
  .panel {
    position: relative; overflow: hidden;
    background: var(--box-black);
    display: flex; flex-direction: column; align-items: center; justify-content: center;
    box-shadow: 0 10px 30px rgba(0,0,0,0.25);
  }
  .panel__sheen {
    position: absolute; inset: 0; width: 100%; height: 100%;
  }
  .panel--lid { width: 440px; height: 377px; }
  .panel--front { width: 440px; height: 168px; }
  .brand-name {
    position: relative; color: var(--gold);
    font-weight: 600; letter-spacing: 0.04em; white-space: nowrap;
  }
  .panel--lid .brand-name { font-size: 48px; }
  .panel--front .brand-name { font-size: 30px; }
  .brand-rule {
    position: relative; display: block; height: 2px; background: var(--gold);
    margin: 10px 0 14px;
  }
  .panel--lid .brand-rule { width: 70px; }
  .panel--front .brand-rule { width: 40px; margin: 6px 0 12px; }
  .tagline {
    position: relative; color: var(--gold);
    font-weight: 700; font-size: 22px; letter-spacing: 0.1em;
  }
  .pack-count {
    position: relative; color: var(--gold-light);
    font-weight: 600; font-size: 13px; letter-spacing: 0.03em;
  }
</style>
</head>
<body>
  <main class="dieline">
    <section class="panel panel--lid" aria-label="Box lid">
      <svg class="panel__sheen" viewBox="0 0 440 377" preserveAspectRatio="none" aria-hidden="true">
        <ellipse cx="220" cy="188" rx="300" ry="110" transform="rotate(-12 220 188)" fill="var(--box-sheen)" opacity="0.85"/>
      </svg>
      <h1 class="brand-name">Leaf of Rivo</h1>
      <span class="brand-rule"></span>
      <p class="tagline">LUXURY TEA</p>
    </section>

    <section class="panel panel--front" aria-label="Box front">
      <svg class="panel__sheen" viewBox="0 0 440 168" preserveAspectRatio="none" aria-hidden="true">
        <ellipse cx="220" cy="84" rx="280" ry="55" transform="rotate(-6 220 84)" fill="var(--box-sheen)" opacity="0.6"/>
      </svg>
      <h2 class="brand-name">Leaf of Rivo</h2>
      <span class="brand-rule"></span>
      <p class="pack-count">100 Leaf of Rivo Tea Filters</p>
    </section>
  </main>
</body>
</html>
```